Stationary and design update for my brand

I need new letterhead, a new business card, business envelope design, new keynote and powerpoint branded slides (16x9). I have logo samples in various styles and brand standards for fonts and colors.

Font styles to use
Sans Serif

```html
<!DOCTYPE html>
<html lang="en">
<head>
<meta charset="utf-8">
<title>Ridgeline Business Card</title>
<link rel="stylesheet" href="https://fonts.googleapis.com/css2?family=Arimo:wght@400&family=Roboto+Slab:wght@400&display=swap">
<style>
  :root {
    --backdrop: #2b2b2d;
    --brand-orange: #ec8d22;
    --card-white: #f6f6f7;
    --ink: #1e1e1e;
    --rule: #555555;
  }
  html, body {
    margin: 0;
    padding: 0;
    width: 1200px;
    height: 779px;
    overflow: hidden;
    background: var(--backdrop);
  }
  .canvas {
    position: relative;
    width: 1200px;
    height: 779px;
  }
  .card {
    position: absolute;
    box-sizing: border-box;
    box-shadow: 0 10px 30px rgba(0,0,0,0.45);
  }
  .card-front {
    left: 90px;
    top: 240px;
    width: 525px;
    height: 300px;
    background: var(--brand-orange);
    color: #ffffff;
    display: flex;
    flex-direction: column;
    align-items: center;
    justify-content: center;
  }
  .brand-name {
    font-family: "Roboto Slab", serif;
    font-weight: 400;
    font-size: 64px;
    letter-spacing: 2px;
    line-height: 1;
    margin-top: 10px;
  }
  .front-web {
    font-family: "Roboto Slab", serif;
    font-size: 14px;
    letter-spacing: 5px;
    margin-top: 44px;
  }
  .card-back {
    left: 760px;
    top: 127px;
    width: 300px;
    height: 525px;
    background: var(--card-white);
    border-bottom: 4px solid var(--brand-orange);
    padding: 0 40px;
    font-family: "Arimo", sans-serif;
    color: var(--ink);
  }
  .back-brand {
    position: absolute;
    right: 40px;
    top: 64px;
    font-family: "Roboto Slab", serif;
    font-size: 20px;
    color: var(--brand-orange);
    letter-spacing: 1px;
  }
  .holder {
    position: absolute;
    left: 40px;
    top: 290px;
    right: 30px;
  }
  .holder-name {
    font-family: "Roboto Slab", serif;
    font-size: 17px;
    color: var(--brand-orange);
    text-transform: uppercase;
    margin: 0;
  }
  .holder-title {
    font-size: 13px;
    margin: 4px 0 0;
  }
  .divider {
    width: 40px;
    height: 1px;
    background: var(--rule);
    margin: 14px 0;
  }
  .address, .contacts {
    font-size: 15px;
    line-height: 1.35;
    margin: 0;
  }
  .contacts .label {
    color: var(--brand-orange);
    display: inline-block;
    width: 26px;
  }
</style>
</head>
<body>
<main class="canvas">
  <section class="card card-front">
    <div class="brand-name">RIDGELINE</div>
    <div class="front-web">WWW.RIDGELINE.COM</div>
  </section>

  <section class="card card-back">
    <div class="back-brand">Ridgeline</div>
    <div class="holder">
      <p class="holder-name">Dana Whitcombe</p>
      <p class="holder-title">Chief of Staff</p>
      <div class="divider"></div>
      <p class="address">418 Harbor Ave, Suite 210<br>Lakeview, NC 28555</p>
      <div class="divider"></div>
      <p class="contacts">
        <span class="label">P :</span>(555)014-2087<br>
        <span class="label">E :</span>dana@ridgeline.com<br>
        <span class="label">W :</span>www.ridgeline.com
      </p>
    </div>
  </section>
</main>
</body>
</html>
```